I need a simple infographic that describes the 4 basic elements of how to effectively create change.

The overall title (Gentle Pressure Relentlessly Applied) should be at the top of the infographic. Subtitle is: "Leading Change".
There are four steps:
1. Alignment- Agreement on Approach
2. Transparency- Metrics for Assurance
3. Skills- Training and Coaching
4. Integrity- Culture of Accountability

Target Market(s)

Business Leaders in a training workshop

Font styles to use
Serif

Requirements
Must have
• Here are the 4 elements of the Infographic: Please show them in order.
• 1. Agreement on Approach. (Alignment)
• 2. Metrics for Assurance (Transparency)
• 3. Training and Coaching (Skills)
• 4. Culture of Accountability (Integrity)
Nice to have
• Cool Graphics that depict the 4 steps.
Should not have
• Pictures.

```html
<!DOCTYPE html>
<html lang="en">
<head>
<meta charset="utf-8">
<title>Gentle Pressure Relentlessly Applied – Leading Change</title>
<link href="https://fonts.googleapis.com/css2?family=Raleway:wght@400;500;600&display=swap" rel="stylesheet">
<style>
  :root {
    --canvas: #e9ecef;
    --navy: #272c3b;
    --navy-deep: #222735;
    --cyan: #17b9d7;
    --white: #ffffff;
    --ink: #2f3338;
    --rule-light: #9aa0a6;
    --tint: #e6f7fb;
  }
  * { box-sizing: border-box; margin: 0; padding: 0; }
  html, body { width: 1036px; height: 1200px; overflow: hidden; }
  body {
    background: var(--canvas);
    font-family: "Raleway", Arial, sans-serif;
    position: relative;
  }
  .slide {
    position: absolute;
    left: 38px;
    width: 960px;
    height: 540px;
    overflow: hidden;
    --text: var(--white);
    --rule: var(--white);
    color: var(--text);
  }
  .slide--dark {
    top: 40px;
    background: linear-gradient(135deg, var(--navy) 0%, var(--navy) 60%, var(--navy-deep) 60%, var(--navy-deep) 100%);
  }
  .slide--light {
    top: 620px;
    background: linear-gradient(120deg, var(--tint) 0%, var(--white) 38%, var(--white) 100%);
    --text: var(--ink);
    --rule: var(--rule-light);
  }
  .brand {
    position: absolute; top: 26px; left: 0; right: 0;
    display: flex; justify-content: center; align-items: center; gap: 10px;
    font-size: 22px; font-weight: 500; letter-spacing: 0.5px;
  }
  .brand-dot {
    width: 26px; height: 26px; border-radius: 50%;
    background: var(--text);
  }
  .title {
    position: absolute; top: 68px; left: 0; right: 0;
    text-align: center; font-size: 25px; font-weight: 500; letter-spacing: 0.3px;
  }
  .title-rule {
    position: absolute; top: 106px; left: 168px; width: 624px;
    height: 2px; background: var(--rule);
  }
  .title-rule::before, .title-rule::after {
    content: ""; position: absolute; top: -3px;
    width: 8px; height: 8px; border-radius: 50%; background: var(--rule);
  }
  .title-rule::before { left: -4px; }
  .title-rule::after { right: -4px; }
  .subtitle {
    position: absolute; top: 124px; left: 0; right: 0;
    text-align: center; font-size: 24px; color: var(--cyan);
  }
  .step {
    position: absolute; top: 170px; width: 200px;
    color: var(--cyan);
  }
  .step-number {
    position: absolute; top: 0; left: 80px;
    width: 40px; height: 40px; border: 2px solid var(--cyan); border-radius: 50%;
    display: flex; align-items: center; justify-content: center;
    font-size: 19px; font-weight: 500;
  }
  .step-ring { position: absolute; top: 40px; left: 0; width: 200px; height: 200px; }
  .step-name {
    position: absolute; top: 254px; left: 32px; width: 136px; height: 28px;
    border-radius: 14px; background: var(--cyan); color: var(--white);
    display: flex; align-items: center; justify-content: center;
    font-size: 16px; font-weight: 600;
  }
  .step-text {
    position: absolute; top: 292px; left: 0; width: 200px;
    text-align: center; font-size: 16px; line-height: 20px; color: var(--text);
  }
  .step--1 { left: 96px; }
  .step--2 { left: 286px; }
  .step--3 { left: 472px; }
  .step--4 { left: 660px; }
  .sprites { position: absolute; width: 0; height: 0; }
</style>
</head>
<body>

<svg class="sprites" aria-hidden="true">
  <defs>
    <symbol id="ring" viewBox="0 0 200 200">
      <g fill="none" stroke="currentColor" stroke-width="2.5">
        <path d="M100 12 A88 88 0 0 0 100 188"/>
        <path d="M100 188 A88 88 0 0 0 100 12" stroke-dasharray="7 6"/>
        <circle cx="100" cy="100" r="68"/>
        <path d="M100 46 A54 54 0 0 1 154 100" stroke-dasharray="5 5" stroke-width="2"/>
        <path d="M100 154 A54 54 0 0 1 46 100" stroke-dasharray="5 5" stroke-width="2"/>
      </g>
      <path d="M181 96 L195 96 L188 108 Z" fill="currentColor"/>
    </symbol>
    <symbol id="icon-align" viewBox="0 0 60 60">
      <g stroke="currentColor" stroke-width="5" stroke-linecap="round">
        <line x1="8" y1="10" x2="52" y2="10"/>
        <line x1="14" y1="22" x2="46" y2="22"/>
        <line x1="8" y1="34" x2="52" y2="34"/>
        <line x1="14" y1="46" x2="46" y2="46"/>
      </g>
    </symbol>
    <symbol id="icon-metrics" viewBox="0 0 60 60">
      <g fill="none" stroke="currentColor" stroke-width="2.5" stroke-linecap="round">
        <rect x="14" y="6" width="34" height="42" rx="2"/>
        <line x1="38" y1="16" x2="44" y2="16"/>
        <line x1="38" y1="40" x2="44" y2="40"/>
        <circle cx="26" cy="26" r="13"/>
        <line x1="35" y1="35" x2="50" y2="52" stroke-width="4"/>
      </g>
    </symbol>
    <symbol id="icon-skills" viewBox="0 0 60 60">
      <g fill="none" stroke="currentColor" stroke-width="2.5" stroke-linecap="round">
        <circle cx="30" cy="26" r="12"/>
        <circle cx="30" cy="26" r="4"/>
        <line x1="30" y1="6" x2="30" y2="10"/>
        <line x1="30" y1="42" x2="30" y2="46"/>
        <line x1="10" y1="26" x2="14" y2="26"/>
        <line x1="46" y1="26" x2="50" y2="26"/>
        <line x1="16" y1="12" x2="19" y2="15"/>
        <line x1="41" y1="37" x2="44" y2="40"/>
        <line x1="44" y1="12" x2="41" y2="15"/>
        <line x1="19" y1="37" x2="16" y2="40"/>
        <line x1="30" y1="46" x2="30" y2="54"/>
        <circle cx="30" cy="56" r="2"/>
      </g>
    </symbol>
    <symbol id="icon-integrity" viewBox="0 0 60 60">
      <g fill="none" stroke="currentColor" stroke-width="2.5" stroke-linecap="round" stroke-linejoin="round">
        <path d="M30 6 L50 13 V29 C50 42 41 50 30 54 C19 50 10 42 10 29 V13 Z"/>
        <path d="M21 30 L28 37 L40 23"/>
      </g>
    </symbol>
  </defs>
</svg>

<section class="slide slide--dark">
  <div class="brand"><span class="brand-dot"></span><span>THE HARLOW GROUP</span></div>
  <h1 class="title">GENTLE PRESSURE RELENTLESSLY APPLIED</h1>
  <div class="title-rule"></div>
  <p class="subtitle">"Leading Change"</p>

  <div class="step step--1">
    <div class="step-number">1</div>
    <svg class="step-ring" viewBox="0 0 200 200"><use href="#ring"/><circle cx="8" cy="100" r="6" fill="none" stroke="currentColor" stroke-width="2.5"/><use href="#icon-align" x="70" y="70" width="60" height="60"/></svg>
    <div class="step-name">Alignment</div>
    <p class="step-text">Agreement<br>on Approach</p>
  </div>
  <div class="step step--2">
    <div class="step-number">2</div>
    <svg class="step-ring" viewBox="0 0 200 200"><use href="#ring"/><use href="#icon-metrics" x="70" y="70" width="60" height="60"/></svg>
    <div class="step-name">Transparency</div>
    <p class="step-text">Metrics<br>for Assurance</p>
  </div>
  <div class="step step--3">
    <div class="step-number">3</div>
    <svg class="step-ring" viewBox="0 0 200 200"><use href="#ring"/><use href="#icon-skills" x="70" y="70" width="60" height="60"/></svg>
    <div class="step-name">Skills</div>
    <p class="step-text">Training<br>and Coaching</p>
  </div>
  <div class="step step--4">
    <div class="step-number">4</div>
    <svg class="step-ring" viewBox="0 0 200 200"><use href="#ring"/><use href="#icon-integrity" x="70" y="70" width="60" height="60"/></svg>
    <div class="step-name">Integrity</div>
    <p class="step-text">Culture<br>of Accountability</p>
  </div>
</section>

<section class="slide slide--light">
  <div class="brand"><span class="brand-dot"></span><span>THE HARLOW GROUP</span></div>
  <h2 class="title">GENTLE PRESSURE RELENTLESSLY APPLIED</h2>
  <div class="title-rule"></div>
  <p class="subtitle">"Leading Change"</p>

  <div class="step step--1">
    <div class="step-number">1</div>
    <svg class="step-ring" viewBox="0 0 200 200"><use href="#ring"/><circle cx="8" cy="100" r="6" fill="none" stroke="currentColor" stroke-width="2.5"/><use href="#icon-align" x="70" y="70" width="60" height="60"/></svg>
    <div class="step-name">Alignment</div>
    <p class="step-text">Agreement<br>on Approach</p>
  </div>
  <div class="step step--2">
    <div class="step-number">2</div>
    <svg class="step-ring" viewBox="0 0 200 200"><use href="#ring"/><use href="#icon-metrics" x="70" y="70" width="60" height="60"/></svg>
    <div class="step-name">Transparency</div>
    <p class="step-text">Metrics<br>for Assurance</p>
  </div>
  <div class="step step--3">
    <div class="step-number">3</div>
    <svg class="step-ring" viewBox="0 0 200 200"><use href="#ring"/><use href="#icon-skills" x="70" y="70" width="60" height="60"/></svg>
    <div class="step-name">Skills</div>
    <p class="step-text">Training<br>and Coaching</p>
  </div>
  <div class="step step--4">
    <div class="step-number">4</div>
    <svg class="step-ring" viewBox="0 0 200 200"><use href="#ring"/><use href="#icon-integrity" x="70" y="70" width="60" height="60"/></svg>
    <div class="step-name">Integrity</div>
    <p class="step-text">Culture<br>of Accountability</p>
  </div>
</section>

</body>
</html>
```